Global (re)insurance broker needs a business card design

We need a classic business card for our company that is headquartered in SG, with offices in Malaysia and Dubai. We specialise in insurance and reinsurance broking and consultancy for our global clients.

```html
<!DOCTYPE html>
<html lang="en">
<head>
<meta charset="UTF-8">
<title>Meridane Business Card</title>
<link rel="stylesheet" href="https://fonts.googleapis.com/css2?family=Arimo:wght@400;700&display=swap">
<style>
  :root {
    --backdrop: #e4e4e4;
    --card: #333333;
    --card-edge: #2a4cb8;
    --accent-blue: #3556b8;
    --wordmark-green: #cfe3c6;
    --text-light: #f2f2f2;
    --divider: #9a9a9a;
    --deboss: #1c1c1c;
  }
  * { margin: 0; padding: 0; box-sizing: border-box; }
  html, body {
    width: 1200px;
    height: 802px;
    overflow: hidden;
    background: var(--backdrop);
    font-family: "Arimo", Arial, sans-serif;
  }
  .stage {
    position: relative;
    width: 1200px;
    height: 802px;
  }
  .card {
    position: absolute;
    top: 258px;
    width: 500px;
    height: 286px;
    background: var(--card);
    border: 2px solid var(--card-edge);
  }
  .card--front { left: 70px; }
  .card--back { left: 630px; }

  .wordmark {
    position: absolute;
    font-weight: 700;
    letter-spacing: 1px;
    line-height: 1;
  }
  .card--front .wordmark {
    left: 30px;
    top: 124px;
    font-size: 36px;
    color: var(--wordmark-green);
  }
  .card--back .wordmark {
    left: 0;
    right: 0;
    top: 118px;
    text-align: center;
    font-size: 52px;
    color: var(--deboss);
  }
  .divider {
    position: absolute;
    left: 250px;
    top: 62px;
    width: 1px;
    height: 164px;
    background: var(--divider);
  }
  .contact {
    position: absolute;
    left: 268px;
    top: 62px;
    color: var(--text-light);
    font-size: 13px;
    line-height: 1.3;
  }
  .contact__name {
    color: var(--accent-blue);
    font-weight: 700;
    font-size: 16px;
    letter-spacing: 0.5px;
    text-transform: uppercase;
  }
  .contact__role { margin-bottom: 10px; }
  .contact__address { margin-bottom: 10px; }
  .contact__line {
    display: flex;
    align-items: center;
    gap: 7px;
  }
  .contact__line svg {
    width: 11px;
    height: 11px;
    flex: none;
  }
</style>
</head>
<body>
<main class="stage">
  <section class="card card--front">
    <div class="wordmark">MERIDANE</div>
    <div class="divider"></div>
    <div class="contact">
      <div class="contact__name">Daniel Hartwell</div>
      <div class="contact__role">Manager</div>
      <div class="contact__address">Your Address, City<br>State, Zip 0000</div>
      <div class="contact__line">
        <svg viewBox="0 0 12 12" aria-hidden="true"><path d="M3 1.5 L4.6 3.6 L3.6 4.8 C4.3 6.3 5.6 7.6 7.2 8.4 L8.4 7.4 L10.5 9 L9.6 10.6 C5.5 10.3 1.7 6.5 1.4 2.4 Z" fill="var(--text-light)"/></svg>
        <span>123-456-2100</span>
      </div>
      <div class="contact__line">
        <svg viewBox="0 0 12 12" aria-hidden="true"><rect x="1" y="2.5" width="10" height="7" fill="none" stroke="var(--text-light)" stroke-width="1"/><path d="M1 2.5 L6 6.5 L11 2.5" fill="none" stroke="var(--text-light)" stroke-width="1"/></svg>
        <span>youremail@example.com</span>
      </div>
      <div class="contact__line">
        <svg viewBox="0 0 12 12" aria-hidden="true"><circle cx="6" cy="6" r="5" fill="none" stroke="var(--text-light)" stroke-width="1"/><ellipse cx="6" cy="6" rx="2.2" ry="5" fill="none" stroke="var(--text-light)" stroke-width="0.8"/><path d="M1 6 H11" stroke="var(--text-light)" stroke-width="0.8"/></svg>
        <span>www.yourwebsite.com</span>
      </div>
    </div>
  </section>

  <section class="card card--back">
    <div class="wordmark">MERIDANE</div>
  </section>
</main>
</body>
</html>
```